Accounting firm for Dentists needs a brochure

We are an accounting firm that specializes in dental practices. We have the information we want attached in a word file. We don't care the number of folds. We would just like it to look professional. Our logo is also attached so you know what our company colors are.

Accounting

```html
<!DOCTYPE html>
<html lang="en">
<head>
<meta charset="utf-8">
<title>BrightMolar Dental CPAs Ltd — Brochure</title>
<link href="https://fonts.googleapis.com/css2?family=Open+Sans:ital,wght@0,400;0,600;0,700;0,800;1,600&family=Raleway:wght@600;700;800&display=swap" rel="stylesheet">
<style>
  :root{
    --blue:#1f9ad6;
    --blue-dark:#0f6aa6;
    --blue-pale:#e3f2fb;
    --ink:#4a5560;
    --ink-soft:#7b8690;
    --paper:#ffffff;
    --stage:#e6e9ec;
    --photo-a:#b9c9d6;
    --photo-b:#e9d6c4;
  }
  *{box-sizing:border-box;margin:0;padding:0}
  html,body{width:889px;height:1200px;overflow:hidden}
  body{background:var(--stage);font-family:"Open Sans",Arial,sans-serif;color:var(--ink);position:relative}

  .sheet{position:absolute;left:27px;width:835px;height:505px;background:var(--paper);
    box-shadow:0 6px 18px rgba(0,0,0,.18);display:flex;overflow:hidden}
  .sheet--front{top:68px}
  .sheet--inside{top:640px}
  .panel{position:relative;width:278.33px;height:100%;overflow:hidden}
  .panel + .panel{border-left:1px solid #e3e7ea}

  .photo{position:absolute;display:block}
  .wave{position:absolute;left:0;width:100%;display:block}

  .band-heading{position:absolute;left:0;background:var(--blue);color:#fff;
    font-family:"Raleway",sans-serif;font-weight:800;font-size:13px;letter-spacing:.5px;
    padding:6px 18px;text-transform:uppercase}

  .copy{font-size:8.6px;line-height:1.5;color:var(--ink)}
  .section-title{font-family:"Raleway",sans-serif;font-weight:800;font-size:11.5px;color:var(--blue);
    text-transform:uppercase;letter-spacing:.4px;margin:0 0 3px}
  .section{margin-bottom:13px}

  /* front left */
  .services-intro{position:absolute;left:18px;right:18px;top:214px}
  .services-list{list-style:none;margin-top:8px}
  .services-list li{font-size:8.6px;line-height:1.7;padding-left:11px;position:relative}
  .services-list li::before{content:"";position:absolute;left:0;top:5px;width:5px;height:5px;background:var(--blue);border-radius:50%}
  .web{position:absolute;left:0;right:0;bottom:14px;text-align:center;color:#fff;font-weight:700;font-size:13px}

  /* front middle */
  .intro{position:absolute;left:22px;right:22px;top:24px;font-size:9px;line-height:1.55;text-align:center}
  .question{position:absolute;left:18px;right:18px;top:128px;background:var(--blue-pale);padding:18px 16px;
    text-align:center;font-style:italic;font-weight:600;color:var(--blue-dark);font-size:11.5px;line-height:1.5}
  .quote-btn{position:absolute;left:40px;right:40px;top:238px;background:var(--paper);border:2px solid var(--blue);
    text-align:center;padding:8px 6px;font-size:9.5px;font-weight:600;color:var(--blue-dark);line-height:1.35}
  .quote-btn strong{display:block;font-weight:800;text-transform:uppercase;font-size:10px}
  .contact{position:absolute;left:0;right:0;top:305px;text-align:center}
  .contact p{font-weight:700;color:var(--blue-dark);font-size:12px;line-height:1.8;display:flex;align-items:center;justify-content:center;gap:6px}
  .contact svg{width:12px;height:12px}

  /* front right (cover) */
  .brand{position:absolute;right:20px;top:22px;text-align:right;display:flex;align-items:center;gap:8px}
  .brand-mark{width:14px;height:14px;background:var(--blue);border-radius:50%}
  .brand-name{font-family:"Raleway",sans-serif;font-weight:800;font-size:21px;color:var(--blue-dark);line-height:1.05}
  .brand-name span{display:block;font-size:11px}
  .tagline{position:absolute;left:0;right:0;bottom:22px;text-align:center;color:#fff;padding:0 22px}
  .tagline h2{font-family:"Raleway",sans-serif;font-weight:800;font-size:12.5px;letter-spacing:.6px}
  .tagline p{font-size:8.4px;line-height:1.4;margin-top:4px}

  /* inside */
  .inside-col{position:absolute;left:18px;right:18px;top:52px}
  .inside-col--plain{top:20px}
  .tax{position:absolute;left:18px;right:18px;top:166px}
</style>
</head>
<body>

<!-- FRONT SHEET -->
<section class="sheet sheet--front" aria-label="Brochure outer side">
  <div class="panel panel--services">
    <svg class="photo" style="left:0;top:0" width="279" height="185" role="img" aria-label="Photo of a smiling family group">
      <defs><linearGradient id="g1" x1="0" y1="0" x2="1" y2="1"><stop offset="0" stop-color="#cfdbe4"/><stop offset="1" stop-color="#e8d2bf"/></linearGradient></defs>
      <rect width="279" height="185" fill="url(#g1)"/>
    </svg>
    <h2 class="band-heading" style="top:182px">Our Services</h2>
    <div class="services-intro copy">
      <p>Our team offers a complete range of accounting services built for dental practices.</p>
      <p style="margin-top:6px">Examples of services available include, but are not limited to:</p>
      <ul class="services-list">
        <li>Monthly Bookkeeping</li>
        <li>Bookkeeper Oversight</li>
        <li>Accounting for Dentists</li>
        <li>Personal Bookkeeping</li>
        <li>Bill Payment and Document Management</li>
        <li>Tax Planning</li>
        <li>Tax Preparation</li>
        <li>Dentistry Industry Comparisons</li>
      </ul>
    </div>
    <svg class="wave" style="bottom:0" width="279" height="70" viewBox="0 0 279 70" preserveAspectRatio="none" aria-hidden="true">
      <path d="M0 22 C80 0 180 38 279 10 V70 H0Z" fill="var(--blue)"/>
    </svg>
    <p class="web">www.brightmolarltd.com</p>
  </div>

  <div class="panel panel--contact">
    <p class="intro">At BrightMolar Dental CPAs Ltd, our licensed CPAs have the knowledge to bridge complex accounting issues and the experience to present a clear picture of your financial position.</p>
    <p class="question">Why not let an independent consultant help you make financial decisions as you focus on growing your practice?</p>
    <p class="quote-btn">Call or email for a <strong>Free quote and consultation</strong></p>
    <div class="contact">
      <p><svg viewBox="0 0 24 24" aria-hidden="true"><path fill="var(--blue)" d="M6.6 10.8a15 15 0 0 0 6.6 6.6l2.2-2.2a1 1 0 0 1 1-.25 11.4 11.4 0 0 0 3.6.57 1 1 0 0 1 1 1V20a1 1 0 0 1-1 1A17 17 0 0 1 3 4a1 1 0 0 1 1-1h3.5a1 1 0 0 1 1 1c0 1.25.2 2.45.57 3.57a1 1 0 0 1-.25 1z"/></svg>1-800-555-0142</p>
      <p><svg viewBox="0 0 24 24" aria-hidden="true"><path fill="var(--blue)" d="M3 5h18v14H3z"/><path d="M3 5l9 7 9-7" stroke="#fff" stroke-width="1.6" fill="none"/></svg>info@brightmolarltd.com</p>
    </div>
    <svg class="wave" style="bottom:0" width="279" height="60" viewBox="0 0 279 60" preserveAspectRatio="none" aria-hidden="true">
      <path d="M0 30 C90 8 190 44 279 18 V60 H0Z" fill="var(--blue-pale)"/>
    </svg>
  </div>

  <div class="panel panel--cover">
    <div class="brand">
      <span class="brand-mark" aria-hidden="true"></span>
      <p class="brand-name">BrightMolar Dental<span>CPAs Ltd</span></p>
    </div>
    <svg class="photo" style="left:0;top:88px" width="279" height="320" role="img" aria-label="Photo of a happy smiling couple">
      <defs><linearGradient id="g2" x1="0" y1="0" x2="1" y2="1"><stop offset="0" stop-color="#d8e3ea"/><stop offset="1" stop-color="#e6cdb6"/></linearGradient></defs>
      <rect width="279" height="320" fill="url(#g2)"/>
    </svg>
    <svg class="wave" style="bottom:0" width="279" height="130" viewBox="0 0 279 130" preserveAspectRatio="none" aria-hidden="true">
      <path d="M0 40 C90 8 190 56 279 20 V130 H0Z" fill="var(--blue-dark)" opacity=".55"/>
      <path d="M0 54 C90 22 190 70 279 36 V130 H0Z" fill="var(--blue)"/>
    </svg>
    <div class="tagline">
      <h2>NO MATTER WHAT YOUR NEEDS</h2>
      <p>We are committed to delivering accurate, timely and professional accounting services.</p>
    </div>
  </div>
</section>

<!-- INSIDE SHEET -->
<section class="sheet sheet--inside" aria-label="Brochure inner side">
  <svg class="photo" style="left:0;top:318px;z-index:0" width="835" height="187" role="img" aria-label="Photo of hands working with a calculator and paperwork">
    <defs><linearGradient id="g3" x1="0" y1="0" x2="1" y2="0"><stop offset="0" stop-color="#eef2f5"/><stop offset=".4" stop-color="#c9d5de"/><stop offset="1" stop-color="#a9b8c4"/></linearGradient></defs>
    <rect width="835" height="187" fill="url(#g3)"/>
  </svg>

  <div class="panel panel--reasons">
    <h2 class="band-heading" style="top:14px">Reasons to Outsource</h2>
    <div class="inside-col copy">
      <div class="section"><h3 class="section-title">Time</h3>
        <p>Our clinical accounting services will save your staff hours each month so they can focus on patient care and daily operations.</p></div>
      <div class="section"><h3 class="section-title">Money</h3>
        <p>Outsourcing costs less than hiring in-house staff, and our fixed monthly fees keep your budget simple and predictable all year.</p></div>
      <div class="section"><h3 class="section-title">Expertise</h3>
        <p>All accounts are handled by CPAs with years of experience serving dental offices, so nothing is left to chance.</p></div>
    </div>
  </div>

  <div class="panel panel--values">
    <div class="inside-col inside-col--plain copy">
      <div class="section"><h3 class="section-title">Excellence</h3>
        <p>We strive for excellence in every engagement and keep our methods current with the latest accounting practices and rules for your practice.</p></div>
      <div class="section"><h3 class="section-title">Timeliness</h3>
        <p>Reports and statements arrive on a schedule you can rely on, giving you the numbers you need when decisions matter most.</p></div>
      <div class="section"><h3 class="section-title">Personalization</h3>
        <p>Every practice is different. We tailor our services to your goals, your team and the way you prefer to work.</p></div>
    </div>
  </div>

  <div class="panel panel--tax">
    <svg class="photo" style="left:0;top:0" width="279" height="150" role="img" aria-label="Photo of a team of business professionals">
      <defs><linearGradient id="g4" x1="0" y1="0" x2="1" y2="1"><stop offset="0" stop-color="#e4e9ee"/><stop offset="1" stop-color="#8fa1b1"/></linearGradient></defs>
      <rect width="279" height="150" fill="url(#g4)"/>
    </svg>
    <div class="tax copy">
      <h3 class="section-title">Advanced Tax Strategies</h3>
      <p>Our planning goes beyond the annual return. We review your structure and identify strategies to reduce taxes and protect the income your practice earns.</p>
    </div>
  </div>

  <svg class="wave" style="top:300px;z-index:1" width="835" height="40" viewBox="0 0 835 40" preserveAspectRatio="none" aria-hidden="true">
    <path d="M278 18 C460 -4 650 34 835 6 V22 C650 46 460 10 278 30Z" fill="var(--blue)"/>
  </svg>
</section>

</body>
</html>
```